One of a Kind Clean Business Card

We need to design a new business card template for our company. Our company designs and produced merchandising displays. You can see a sample of what we produce on our site www.qorvatfixtures.com. I have uploaded our logo in vector format, as well as a picture of our current business cards. We want a totally different look. We want simple and clean, looking forward to seeing what people create.
Updates

I would like to update the address for Tellur Display Group Inc. 418 N Brindle Ave Arlington Heights, IL 60817 Would also note. No QR codes

Industry/Entity Type

Business

Contact Information for Business Card

Need a 1 sided business card designed.

Font styles to use
Serif

Requirements
Must have
• Easy to view; Clean Design
Nice to have
• Features that promote engineering and creativity
Should not have
• Too much clutter, keep it simple

```html
<!DOCTYPE html>
<html lang="en">
<head>
<meta charset="utf-8">
<title>Tellur Display Group Inc. — Business Card, Front and Back</title>
<link href="https://fonts.googleapis.com/css2?family=Roboto:wght@400;700&family=Open+Sans:wght@300&display=swap" rel="stylesheet">
<style>
  :root {
    --stage: #e9e7e4;
    --card-dark: #0a0a0a;
    --card-mid: #1e1e1e;
    --ink: #ffffff;
    --accent: #b01e23;
    --emboss: #3c3c3c;
  }
  html, body {
    margin: 0;
    width: 1200px;
    height: 716px;
    overflow: hidden;
    background: var(--stage);
  }
  .card {
    position: absolute;
    width: 520px;
    height: 297px;
    border-radius: 5px;
    background: linear-gradient(120deg, var(--card-mid) 0%, var(--card-dark) 70%);
    color: var(--ink);
    font-family: "Roboto", sans-serif;
    box-shadow: 0 10px 26px rgba(0,0,0,.28);
  }
  .card-back { left: 50px; top: 70px; }
  .card-front { left: 630px; top: 350px; }

  .back-name {
    position: absolute;
    left: 60px;
    top: 104px;
    width: 400px;
    font-family: "Open Sans", sans-serif;
    font-weight: 300;
    font-size: 30px;
    line-height: 1.2;
    letter-spacing: 1px;
    text-transform: uppercase;
    color: var(--emboss);
  }

  .brand {
    position: absolute;
    left: 28px;
    top: 112px;
    width: 220px;
    font-family: "Open Sans", sans-serif;
    font-weight: 300;
    font-size: 20px;
    line-height: 1.2;
    letter-spacing: .5px;
    text-transform: uppercase;
    color: var(--ink);
  }
  .divider {
    position: absolute;
    left: 262px;
    top: 64px;
    width: 1.5px;
    height: 170px;
    background: var(--accent);
  }
  .contact {
    position: absolute;
    left: 280px;
    top: 62px;
  }
  .contact .name {
    margin: 0;
    font-size: 20px;
    font-weight: 700;
    letter-spacing: .5px;
    text-transform: uppercase;
  }
  .contact .title {
    margin: 2px 0 10px;
    font-size: 12px;
    color: var(--accent);
  }
  .contact .address {
    margin: 0 0 6px;
    font-size: 12px;
    line-height: 1.35;
  }
  .contact ul {
    list-style: none;
    margin: 0;
    padding: 0;
    font-size: 12px;
    line-height: 1.6;
  }
  .contact li {
    display: flex;
    align-items: center;
    gap: 6px;
  }
  .contact svg {
    width: 10px;
    height: 10px;
    flex: none;
    fill: none;
    stroke: var(--accent);
    stroke-width: 2;
  }
</style>
</head>
<body>
  <div class="card card-back">
    <div class="back-name">Tellur Display Group Inc.</div>
  </div>

  <div class="card card-front">
    <div class="brand">Tellur Display Group Inc.</div>
    <div class="divider"></div>
    <div class="contact">
      <h1 class="name">Dana Holloway</h1>
      <p class="title">President &amp; CEO</p>
      <p class="address">418 N Brindle Ave<br>Arlington Heights, IL 60817</p>
      <ul>
        <li>
          <svg viewBox="0 0 24 24" aria-hidden="true"><path d="M5 3h4l2 5-3 2a12 12 0 0 0 6 6l2-3 5 2v4a2 2 0 0 1-2 2A18 18 0 0 1 3 5a2 2 0 0 1 2-2z"/></svg>
          815-555-0142
        </li>
        <li>
          <svg viewBox="0 0 24 24" aria-hidden="true"><rect x="6" y="2" width="12" height="20" rx="2"/><line x1="11" y1="18" x2="13" y2="18"/></svg>
          312-555-0176
        </li>
        <li>
          <svg viewBox="0 0 24 24" aria-hidden="true"><rect x="2" y="5" width="20" height="14" rx="1"/><path d="M2 6l10 7 10-7"/></svg>
          dholloway@qorvatfixtures.com
        </li>
        <li>
          <svg viewBox="0 0 24 24" aria-hidden="true"><circle cx="12" cy="12" r="10"/><path d="M2 12h20M12 2c3 3 3 17 0 20M12 2c-3 3-3 17 0 20"/></svg>
          www.qorvatfixtures.com
        </li>
      </ul>
    </div>
  </div>
</body>
</html>
```